develop our online residential property development appraisal service

This project requires a detailed WordPress design to represent a new digital residential property development consultancy business. At its heart it will have a number of different products that essentially advise customers of the potential value and feasibility of developing their residential site into multiple townhouses, units, apartments, etc... This will be accompanied by explaining the considerations of residential property development.

We aim to navigate and break down this complex area and provide our customers with the tools, knowledge, control and power to 'unlock the value' in their property.

REFERENCE DOCUMENTS:
1. Detailed solution requirements please refer to the attached 'wordpressdesignrequirements'
2. Logo files, style guide and colour pallet please refer to the attached 'QRBT.zip'
3. Site Map refer to attached 'wordpressdesignsitemap'
Updates

Reason: Additional information provided so extending period for designs to take into account.

Target Market(s)

The site will appeal to professional service providers; accountants, financial planners, lawyers, etc…

Industry/Entity Type

Residential

Font styles to use
Sans Serif
Other font styles liked:
• Similar to the logo font, slim line and simple

Requirements
Must have
• The logo, style and colour palette provided in the attached 'QRBT.zip' files
• Satisfy the intent of the 'wordpressdesignrequirements'
• Present as an online-centric business
• Clean, crisp and modern design
• Predominant use of white as a background contrasted with the colours provided in the colour palette
Nice to have
• Use of the following WordPress business themes is encouraged but not mandatory:
• 1. Tovy
• 2. Palex
• 3. Munk
Should not have
• Overt references to Australia

```html
<!DOCTYPE html>
<html lang="en">
<head>
<meta charset="utf-8">
<title>QRBT – Development Appraisals</title>
<link rel="stylesheet" href="https://fonts.googleapis.com/css2?family=Open+Sans:wght@300;400;600;700&display=swap">
<style>
:root{
  --green:#1f9d5c;
  --green-bright:#22a968;
  --ink:#1b1b1b;
  --dark:#1c1c1c;
  --dark-2:#262626;
  --footer:#0d0d0d;
  --white:#ffffff;
  --text:#222222;
}
*{box-sizing:border-box;margin:0;padding:0}
html,body{width:1200px;height:3035px;overflow:hidden}
body{font-family:"Open Sans",Arial,sans-serif;color:var(--text);background:var(--white);position:relative}
.abs{position:absolute}
a{color:inherit;text-decoration:none}
.btn{position:absolute;background:var(--green);color:var(--white);font-weight:600;display:flex;align-items:center;justify-content:center;border-radius:2px}

/* header */
.topbar{left:0;top:0;width:1200px;height:101px;background:linear-gradient(90deg,#1a9a5a,#15a28f 60%,#1a9a5a)}
.navbar{left:99px;top:28px;width:1002px;height:73px;background:var(--ink);display:flex;align-items:center;padding:0 22px}
.brand{display:flex;align-items:center;gap:10px;color:var(--green-bright);font-size:26px;font-weight:600;letter-spacing:1px}
.brand-mark{width:12px;height:12px;border-radius:50%;background:var(--green-bright)}
.menu{margin-left:auto;display:flex;gap:30px;color:#e8e8e8;font-size:14px}
.search{margin-left:22px;width:30px;height:30px;border-radius:50%;background:var(--green-bright);display:flex;align-items:center;justify-content:center}

/* hero */
.hero{left:0;top:101px;width:1200px;height:522px;background:linear-gradient(180deg,#6f8f4c 0%,#8c6a4e 45%,#5d8a2e 75%,#4f7f25 100%)}
.hero-title{left:0;top:392px;width:1200px;text-align:center;color:var(--white);font-size:37px;font-weight:300}
.dots{left:566px;top:591px;display:flex;gap:6px}
.dots span{width:10px;height:10px;border-radius:50%;background:#2c2c2c}
.dots span:first-child{background:var(--green-bright)}

/* video */
.video{left:0;top:623px;width:1200px;height:436px;background:linear-gradient(180deg,var(--dark) 0 66%,var(--dark-2) 66% 100%)}
.video-heading{left:123px;top:680px;width:360px;font-size:40px;font-weight:300;line-height:46px;color:var(--white)}
.video-heading em{font-style:normal;color:var(--green-bright);display:block}
.video-btn{left:123px;top:929px;width:256px;height:57px;font-size:18px;font-weight:700;letter-spacing:-.5px}
.video-frame{left:504px;top:658px;width:585px;height:338px;background:#e9e9e9;padding:8px;box-shadow:0 18px 24px rgba(0,0,0,.55)}
.video-still{width:100%;height:100%;background:linear-gradient(180deg,#c9866a 0%,#8a5540 45%,#4f6b35 75%,#3e4a3a 100%);display:flex;align-items:center;justify-content:center}

/* property report */
.section-title{left:0;width:1200px;text-align:center;font-size:40px;font-weight:300;color:#1a1a1a}
.intro{left:80px;top:1164px;width:1040px;text-align:center;font-size:14px;line-height:24px;color:#222}
.card-img{top:1243px;width:310px;height:180px}
.card-title{top:1441px;font-size:20px;font-weight:400;color:#111}
.card-title b,.about-title b{color:var(--green);font-weight:600}
.card-text{top:1488px;width:310px;font-size:12px;line-height:21px;letter-spacing:-.2px;color:#222}
.card-btn{top:1617px;width:198px;height:43px;font-size:13px}

/* family band */
.band{left:0;top:1751px;width:1200px;height:575px;background:linear-gradient(90deg,#6b5446 0%,#a88a73 35%,#7a6a5c 60%,#8a9a6a 85%,#6e8a45 100%)}
.band-box{left:698px;top:1828px;width:391px;height:431px;background:rgba(35,35,35,.82);padding:44px 24px 0}
.band-title{font-size:40px;font-weight:700;line-height:43px;color:var(--green-bright)}
.band-title span{color:var(--white)}
.band-text{margin-top:22px;font-size:13px;line-height:24px;color:#e6e6e6}
.band-btn{left:727px;top:2187px;width:122px;height:40px;font-size:13px}

/* about */
.about-title{top:2454px;font-size:20px;font-weight:600;color:#111}
.about-text{top:2506px;width:310px;font-size:12px;line-height:21px;letter-spacing:-.2px;color:#222}
.about-btn{top:2639px;width:122px;height:40px;font-size:13px}

/* footer */
.footer{left:0;top:2747px;width:1200px;height:288px;background:var(--footer)}
.foot-links{top:2795px;list-style:none;font-size:13.5px;line-height:30.5px;color:#d8d8d8}
.foot-head{font-size:14px;color:#cfcfcf}
.social{display:flex;gap:12px;margin-top:10px}
.social span{width:10px;height:10px;border-radius:50%;background:#6e6e6e}
.copyright{left:0;top:2986px;width:1200px;text-align:center;font-size:11px;color:#bbb}
</style>
</head>
<body>

<div class="abs topbar"></div>
<header class="abs navbar">
  <div class="brand"><span class="brand-mark"></span>QRBT</div>
  <nav class="menu">
    <a>Home</a><a>About Us</a><a>Social Integration</a><a>Property Development Overview</a><a>Contact Us</a>
  </nav>
  <div class="search">
    <svg width="14" height="14" viewBox="0 0 14 14"><circle cx="6" cy="6" r="4" fill="none" stroke="#fff" stroke-width="2"/><line x1="9" y1="9" x2="13" y2="13" stroke="#fff" stroke-width="2"/></svg>
  </div>
</header>

<section class="abs hero" role="img" aria-label="Photo of a brick family house with a large tree and green lawn"></section>
<h1 class="abs hero-title">Northgate Development Appraisals</h1>
<div class="abs dots"><span></span><span></span><span></span><span></span></div>

<section class="abs video"></section>
<h2 class="abs video-heading"><em>What problems</em>we can solve / what opportunities for our products</h2>
<a class="btn video-btn">WATCH THIS VIDEO</a>
<div class="abs video-frame">
  <div class="video-still" role="img" aria-label="Video still of modern brick townhouses at sunset">
    <svg width="106" height="106" viewBox="0 0 106 106"><circle cx="53" cy="53" r="47" fill="none" stroke="#fff" stroke-width="9"/><path d="M42 31 L75 53 L42 75 Z" fill="#fff"/></svg>
  </div>
</div>

<h2 class="abs section-title" style="top:1100px">PROPERTY REPORT</h2>
<p class="abs intro">Lorem Ipsum is simply dummy text of the printing and typesetting industry. Lorem Ipsum has been the industry's standard dummy text ever since the 1500s, when an unknown printer took a galley of type and scrambled it to make a type specimen book.</p>

<div class="abs card-img" style="left:111px;background:linear-gradient(180deg,#6f9fd6,#d8dde2 60%,#8a8a80)" role="img" aria-label="Photo of a modern white house"></div>
<div class="abs card-img" style="left:445px;background:linear-gradient(180deg,#9fc3e6,#8a6b55 55%,#5f8a3a)" role="img" aria-label="Photo of a suburban brick house with garden"></div>
<div class="abs card-img" style="left:779px;background:linear-gradient(180deg,#6aa3dc,#a58670 45%,#4f8f2f)" role="img" aria-label="Photo of a house with flower beds and lawn"></div>

<h3 class="abs card-title" style="left:108px">Property <b>Report A</b></h3>
<h3 class="abs card-title" style="left:445px">Property <b>Report b</b></h3>
<h3 class="abs card-title" style="left:779px">Property <b>Report C</b></h3>

<p class="abs card-text" style="left:111px">Lorem Ipsum is simply dummy text of the printing and typesetting industry. Lorem Ipsum has been the industry's standard dummy text ever since the 1500s, when an unknown printer took a galley of type and scrambled it to make a type specimen book.</p>
<p class="abs card-text" style="left:445px">Lorem Ipsum is simply dummy text of the printing and typesetting industry. Lorem Ipsum has been the industry's standard dummy text ever since the 1500s, when an unknown printer took a galley of type and scrambled it to make a type specimen book.</p>
<p class="abs card-text" style="left:779px">Lorem Ipsum is simply dummy text of the printing and typesetting industry. Lorem Ipsum has been the industry's standard dummy text ever since the 1500s, when an unknown printer took a galley of type and scrambled it to make a type specimen book.</p>

<a class="btn card-btn" style="left:111px">Request Property Report A</a>
<a class="btn card-btn" style="left:445px">Request Property Report B</a>
<a class="btn card-btn" style="left:779px">Request Property Report C</a>

<section class="abs band" role="img" aria-label="Photo of a smiling family in front of their home"></section>
<div class="abs band-box">
  <h2 class="band-title">Property Development <span>Report</span></h2>
  <p class="band-text">Lorem Ipsum is simply dummy text of the printing and typesetting industry. Lorem Ipsum has been the industry's standard dummy text ever since the 1500s, when an unknown printer took a galley of type and scrambled it to make a type specimen book.</p>
</div>
<a class="btn band-btn">Read More</a>

<h2 class="abs section-title" style="top:2356px">ABOUT US</h2>
<h3 class="abs about-title" style="left:114px"><b>WHO</b> are we?</h3>
<h3 class="abs about-title" style="left:446px"><b>WHAT</b> do we do?</h3>
<h3 class="abs about-title" style="left:779px"><b>HOW</b> do we do it?</h3>
<p class="abs about-text" style="left:111px">Lorem Ipsum is simply dummy text of the printing and typesetting industry. Lorem Ipsum has been the industry's standard dummy text ever since the 1500s, when an unknown printer took a galley of type and scrambled it to make a type specimen book.</p>
<p class="abs about-text" style="left:445px">Lorem Ipsum is simply dummy text of the printing and typesetting industry. Lorem Ipsum has been the industry's standard dummy text ever since the 1500s, when an unknown printer took a galley of type and scrambled it to make a type specimen book.</p>
<p class="abs about-text" style="left:779px">Lorem Ipsum is simply dummy text of the printing and typesetting industry. Lorem Ipsum has been the industry's standard dummy text ever since the 1500s, when an unknown printer took a galley of type and scrambled it to make a type specimen book.</p>
<a class="btn about-btn" style="left:111px">Read More</a>
<a class="btn about-btn" style="left:445px">Read More</a>
<a class="btn about-btn" style="left:779px">Read More</a>

<footer class="abs footer"></footer>
<ul class="abs foot-links" style="left:111px">
  <li>Home</li><li>About Us</li><li>Social Integration</li><li>Property Development Overview</li><li>Contact Us</li>
</ul>
<ul class="abs foot-links" style="left:445px">
  <li>E-Mail Collection</li><li>Property Report Page A</li><li>Property Report Page B</li><li>Property Report Page C</li>
</ul>
<div class="abs foot-links" style="left:779px;top:2795px;line-height:normal">
  <div class="foot-head">Contact Us</div>
  <div style="margin-top:16px;display:flex;align-items:center;gap:8px;font-size:13px;color:#d8d8d8">
    <svg width="16" height="12" viewBox="0 0 16 12"><rect x="1" y="1" width="14" height="10" fill="none" stroke="#1f9d5c" stroke-width="1.5"/><path d="M1 1 L8 7 L15 1" fill="none" stroke="#1f9d5c" stroke-width="1.5"/></svg>
    contactus@qrbtappraisals.com
  </div>
  <div class="foot-head" style="margin-top:14px">Connect With Us</div>
  <div class="social"><span></span><span></span><span></span><span></span><span></span></div>
</div>
<p class="abs copyright">© 2015 Company Name .All Rights Reserved</p>

</body>
</html>
```